NEED A BUSINESS CARD FOR A NEW ELECTRICAL BUSINESS

HI I am after a new business card for my new electrical business I have a logo that I have attached its the one in blue, I would like that on the front and on the back my name- Leonard Pike, Email leonardpike@tallmesh.com, mobile 0491362047, licence no# vic 47819, nsw 591304k I wont something that is a stand out from the rest but at the same time is neat as being a new business I wont it to catch peoples eye on the front of the card I would like the logo and not much else.
And on the back as well I would like a slogan saying something like
Quality-Reliable-Service

Hi all on the back of the card I would like a little slogan like Quality-Reliable-Service something like that would be good thanks

Hi all the business card needs to have both these licence numbers on it                                                  VIC-47819 nsw-591304k

```html
<!DOCTYPE html>
<html lang="en">
<head>
<meta charset="utf-8">
<title>Leonard Pike Electrical – Business Card</title>
<link href="https://fonts.googleapis.com/css2?family=Michroma&family=Open+Sans:wght@400;600&display=swap" rel="stylesheet">
<style>
  :root {
    --canvas: #ffffff;
    --card-black: #050505;
    --card-white: #ffffff;
    --silver-light: #d4d5d7;
    --silver-mid: #a9abae;
    --silver-dark: #6f7174;
    --brand-blue: #0d5fb0;
    --text-dark: #1b1b1b;
    --phone-grey: #8d8f92;
  }
  * { box-sizing: border-box; margin: 0; padding: 0; }
  html, body {
    width: 1200px;
    height: 1000px;
    overflow: hidden;
    background: var(--canvas);
  }
  .canvas {
    position: relative;
    width: 1200px;
    height: 1000px;
  }

  /* ---------- Front of card ---------- */
  .card {
    position: absolute;
    width: 760px;
    height: 430px;
    border-radius: 34px;
    overflow: hidden;
  }
  .card-front {
    left: 60px;
    top: 50px;
    background: var(--card-black);
  }
  .front-frame {
    position: absolute;
    left: 55px;
    top: 40px;
    width: 650px;
    height: 350px;
  }
  .brand-lockup {
    position: absolute;
    left: 0;
    right: 0;
    top: 178px;
    display: flex;
    align-items: center;
    justify-content: center;
    gap: 18px;
  }
  .brand-square {
    width: 34px;
    height: 34px;
    background: var(--brand-blue);
  }
  .brand-name {
    font-family: "Michroma", sans-serif;
    font-size: 30px;
    letter-spacing: 1px;
    color: var(--silver-mid);
    white-space: nowrap;
  }

  /* ---------- Back of card ---------- */
  .card-back {
    left: 380px;
    top: 520px;
    background: var(--card-white);
    border: 1px solid #d9d9d9;
  }
  .plug-illustration {
    position: absolute;
    left: 0;
    top: 62px;
    width: 760px;
    height: 258px;
    border-radius: 60px 0 0 60px;
    background: linear-gradient(90deg, #c9cacc 0%, #8f9194 28%, #b5b7ba 45%, #c3c5c7 100%);
  }
  .contact-panel {
    position: absolute;
    left: 220px;
    top: 96px;
    width: 510px;
    height: 160px;
    background: var(--card-white);
    border-radius: 14px;
    padding: 20px 26px;
  }
  .contact-name {
    font-family: "Michroma", sans-serif;
    font-size: 24px;
    letter-spacing: 2px;
    color: var(--brand-blue);
    text-transform: uppercase;
  }
  .contact-phone {
    font-family: "Michroma", sans-serif;
    font-size: 44px;
    line-height: 1.15;
    color: var(--phone-grey);
    margin-top: 4px;
    white-space: nowrap;
  }
  .contact-licence {
    font-family: "Open Sans", sans-serif;
    font-size: 14px;
    letter-spacing: 0.5px;
    color: var(--brand-blue);
    margin-top: 8px;
  }
  .contact-email {
    position: absolute;
    left: 240px;
    top: 270px;
    font-family: "Open Sans", sans-serif;
    font-size: 21px;
    color: var(--text-dark);
  }
  .contact-email .label {
    color: var(--brand-blue);
    font-weight: 600;
    margin-right: 6px;
  }
  .slogan-band {
    position: absolute;
    left: 0;
    bottom: 0;
    width: 100%;
    height: 110px;
    background: var(--card-black);
    display: flex;
    align-items: center;
    justify-content: center;
  }
  .slogan {
    font-family: "Michroma", sans-serif;
    font-size: 28px;
    letter-spacing: 2px;
    color: var(--brand-blue);
    text-transform: uppercase;
  }
</style>
</head>
<body>
<div class="canvas">

  <section class="card card-front" aria-label="Business card front">
    <svg class="front-frame" viewBox="0 0 650 350" aria-hidden="true">
      <defs>
        <linearGradient id="frameSilver" x1="0" y1="0" x2="1" y2="0">
          <stop offset="0" stop-color="#5f6164"/>
          <stop offset="0.45" stop-color="#d4d5d7"/>
          <stop offset="1" stop-color="#8a8c8f"/>
        </linearGradient>
      </defs>
      <rect x="12" y="12" width="626" height="326" rx="60" ry="60"
            fill="none" stroke="url(#frameSilver)" stroke-width="22"/>
    </svg>
    <div class="brand-lockup">
      <span class="brand-square"></span>
      <span class="brand-name">LEONARD PIKE ELECTRICAL</span>
    </div>
  </section>

  <section class="card card-back" aria-label="Business card back">
    <div class="plug-illustration" role="img" aria-label="Grey electrical plug and cable illustration"></div>
    <div class="contact-panel">
      <p class="contact-name">Leonard Pike</p>
      <p class="contact-phone">0491 362 047</p>
      <p class="contact-licence">licence no VIC 47819 NSW 591304K</p>
    </div>
    <p class="contact-email"><span class="label">E</span>leonardpike@tallmesh.com</p>
    <div class="slogan-band">
      <p class="slogan">Quality Reliable Service</p>
    </div>
  </section>

</div>
</body>
</html>
```